FernPivotHub.com needs updated website design.

FernPivotHub.com offers individuals a quick, hassle-free way of selling their car, rv, or boat in the Sun City Center, FL area. We will come to the customer's place of choosing in order to give them an in-person offer for their car, rv, or boat. Looking for a website design that will allow users to input their vehicle details as well as their contact info in order to schedule a time and place for our staff to come make them an offer. Currently have an active site that can be referenced.

Target Market(s)

Older people who no longer need their cars.

Industry/Entity Type

Automotive

Coding

Coded - Design and coding required

Number of Pages Required

3 page

Font styles to use
Sans Serif

Colors
a1cd3a
33b8a4

Requirements
Must have
• Trustworthy theme, Emphasis on capturing contact info (contact form visible at all times). Standard privacy policy. Wordpress theme

```html
<!DOCTYPE html>
<html lang="en">
<head>
<meta charset="utf-8">
<title>FernPivotHub.com – Sell Your Car, RV or Boat</title>
<link href="https://fonts.googleapis.com/css2?family=Poppins:wght@400;500;600;700&family=Open+Sans:wght@400;600&display=swap" rel="stylesheet">
<style>
:root{
  --navy:#13285a;
  --teal:#2fa995;
  --teal-light:#33b8a4;
  --green:#a1cd3a;
  --text:#4a4a4a;
  --grey-panel:#ebebeb;
  --dark:#0f1013;
  --white:#ffffff;
}
*{box-sizing:border-box;margin:0;padding:0}
html,body{width:1200px;height:3660px;overflow:hidden}
body{position:relative;background:var(--white);font-family:"Open Sans",sans-serif;color:var(--text)}
.abs{position:absolute}
.heading{font-family:"Poppins",sans-serif}

/* header */
.brand{left:142px;top:20px}
.brand-row{display:flex;align-items:center;gap:12px}
.brand-name{font-family:"Poppins",sans-serif;font-weight:700;font-size:22px;color:var(--navy)}
.brand-dot{width:46px;height:46px;border-radius:50%;background:var(--teal-light)}
.brand-tag{font-family:"Poppins",sans-serif;font-size:13px;font-weight:600;color:var(--navy);margin-top:-6px}
.phone{left:724px;top:18px;display:flex;align-items:center;gap:8px;font-family:"Poppins",sans-serif;font-size:24px;color:var(--navy)}
.quote-btn{left:920px;top:17px;width:135px;height:34px;border-radius:17px;background:var(--teal);color:#fff;font-family:"Poppins",sans-serif;font-size:14px;display:flex;align-items:center;justify-content:center;gap:6px}
.nav{left:488px;top:64px;display:flex;gap:36px;font-family:"Poppins",sans-serif;font-size:14px;color:var(--navy)}
.nav .active{border-bottom:2px solid var(--navy);padding-bottom:2px}

/* hero */
.hero{left:0;top:95px;width:1200px;height:605px;overflow:hidden}
.hero-photo{position:absolute;inset:0;background:linear-gradient(110deg,#4d5154 0%,#8b9196 40%,#bfc4c8 70%,#8d9398 100%)}
.hero-quote{left:145px;top:128px;font-family:"Poppins",sans-serif;font-size:32px;font-weight:500;color:#fff}
.arrow-btn{width:40px;height:40px;border-radius:50%;background:rgba(255,255,255,.9);display:flex;align-items:center;justify-content:center}
.offer-form{left:728px;top:156px;width:327px;height:398px;background:rgba(255,255,255,.95);padding:18px 15px}
.offer-form h2{font-family:"Poppins",sans-serif;font-weight:500;font-size:24px;line-height:31px;color:var(--navy);text-align:center;margin-bottom:12px}
.field{height:38px;border:1px solid #c9c9c9;border-radius:2px;background:#fff;margin-bottom:10px;display:flex;align-items:center;justify-content:space-between;padding:0 14px;font-size:13px;color:#777}
.field-pair{display:flex;gap:8px}
.field-pair .field{flex:1}
.caret{width:0;height:0;border-left:6px solid transparent;border-right:6px solid transparent;border-top:6px solid #555}
.submit{display:block;margin:12px auto 0;width:96px;height:34px;border-radius:17px;background:var(--teal);color:#fff;font-family:"Poppins",sans-serif;font-size:14px;border:none}

/* welcome */
.welcome-title{left:143px;top:765px;font-family:"Poppins",sans-serif;font-size:34px;font-weight:500;color:var(--navy)}
.welcome-copy{left:143px;top:826px;width:420px;font-size:14px;line-height:27px}
.checks{list-style:none;margin-top:18px}
.checks li{position:relative;padding-left:21px;color:var(--teal);font-family:"Poppins",sans-serif;font-size:14px;line-height:27px;margin-bottom:27px}
.checks li::before{content:"›";position:absolute;left:0;top:0;color:var(--teal)}
.welcome-photo{left:640px;top:775px;width:415px;height:392px;background:linear-gradient(135deg,#2c3e5a,#7f8c98 55%,#c5cbd1)}

/* bands */
.band{left:0;width:1200px}
.band-title{width:1200px;left:0;text-align:center;font-family:"Poppins",sans-serif;font-size:32px;font-weight:500;color:#fff}
.step{width:300px;text-align:center;color:#fff}
.step-icon{width:112px;height:112px;border-radius:50%;background:var(--teal-light);margin:0 auto 14px;display:flex;align-items:center;justify-content:center}
.step-num{font-family:"Poppins",sans-serif;font-size:13px;color:var(--green)}
.step-title{font-family:"Poppins",sans-serif;font-size:21px;font-weight:500;margin:2px 0 4px}
.step-text{font-size:11px;line-height:19px}

/* reviews */
.reviews-title{left:0;width:1200px;top:1806px;text-align:center;font-family:"Poppins",sans-serif;font-size:32px;font-weight:500;color:var(--navy)}
.reviews-text{left:143px;top:1856px;width:914px;text-align:center;font-family:"Poppins",sans-serif;font-size:16px;line-height:32px;color:#333}
.avatar{left:559px;top:1962px;width:80px;height:80px;border-radius:50%;background:linear-gradient(#b9b3ad,#6d6660)}
.reviewer{left:0;width:1200px;top:2050px;text-align:center;font-family:"Poppins",sans-serif;font-size:16px;color:var(--teal)}
.chev{font-size:40px;color:#555;font-family:"Poppins",sans-serif;top:1940px}

/* why choose */
.feature{width:217px;height:152px;background:#fff;top:2340px;text-align:center;padding-top:24px}
.feature h3{font-family:"Poppins",sans-serif;font-size:24px;font-weight:500;color:var(--teal);margin:10px 0 6px}
.feature p{font-size:11px;color:#444}

/* faq */
.faq-title{left:0;width:1200px;top:2718px;text-align:center;font-family:"Poppins",sans-serif;font-size:32px;font-weight:500;color:var(--navy)}
.faq-open{left:143px;top:2780px;width:912px;height:174px;border:1px solid #a7a7a7;padding:22px 28px}
.faq-open h4{font-family:"Poppins",sans-serif;font-size:20px;font-weight:400;color:var(--teal);margin-bottom:12px;display:flex;justify-content:space-between}
.faq-open p{font-size:11px;line-height:24px;color:#333}
.faq-open a{font-size:11px;color:var(--teal)}
.faq-item{left:143px;width:912px;height:64px;background:var(--grey-panel);padding:0 28px;display:flex;align-items:center;justify-content:space-between;font-family:"Poppins",sans-serif;font-size:20px;color:#333}
.plus{width:14px;height:14px;border-radius:50%;background:#333;color:#fff;font-size:12px;line-height:14px;text-align:center;font-family:"Open Sans",sans-serif}
.view-all{left:552px;top:3340px;width:96px;height:34px;border-radius:17px;background:var(--teal);color:#fff;font-family:"Poppins",sans-serif;font-size:14px;display:flex;align-items:center;justify-content:center}

/* footer */
.footer-links{left:143px;top:3558px;font-size:11px;color:#bbb}
.footer-links span{margin:0 6px;color:#777}
.copyright{left:143px;top:3594px;font-size:11px;color:#bbb}
.social{top:3578px;font-size:12px;color:#aaa}
</style>
</head>
<body>

<!-- header -->
<div class="abs brand">
  <div class="brand-row"><span class="brand-name">FernPivotHub.com</span><span class="brand-dot"></span></div>
  <div class="brand-tag">I'll Buy You Car Boat RV Today</div>
</div>
<div class="abs phone">
  <svg width="18" height="18" viewBox="0 0 24 24"><path fill="#13285a" d="M6.6 10.8a15 15 0 0 0 6.6 6.6l2.2-2.2c.3-.3.7-.4 1-.2 1.1.4 2.3.6 3.6.6.6 0 1 .4 1 1V20c0 .6-.4 1-1 1A17 17 0 0 1 3 4c0-.6.4-1 1-1h3.5c.6 0 1 .4 1 1 0 1.3.2 2.5.6 3.6.1.3 0 .7-.2 1z"/></svg>
  555-014-2207
</div>
<div class="abs quote-btn">
  <svg width="12" height="12" viewBox="0 0 24 24"><path fill="none" stroke="#fff" stroke-width="3" d="M4 20h16M5 16l11-11 3 3-11 11H5z"/></svg>
  Get a Quote
</div>
<nav class="abs nav">
  <span class="active">Home</span><span>About Us</span><span>Car</span><span>RV</span><span>Boat</span><span>How It Works</span><span>Contact Us</span>
</nav>

<!-- hero -->
<section class="abs hero">
  <div class="hero-photo" role="img" aria-label="Hand holding out car keys in front of a silver car"></div>
  <svg class="abs" style="left:0;top:505px" width="1200" height="100" viewBox="0 0 1200 100">
    <polygon points="0,23 1200,82 1200,100 0,100" fill="#fff"/>
    <polygon points="0,20 1090,80 1055,100 0,42" fill="#a1cd3a"/>
    <polygon points="0,42 1055,100 0,100" fill="#fff"/>
  </svg>
</section>
<div class="abs hero-quote">“Don’t Sell Til You Give Me A Yell”</div>
<div class="abs arrow-btn" style="left:55px;top:335px"><svg width="16" height="16" viewBox="0 0 16 16"><path d="M10 2 4 8l6 6" fill="none" stroke="#33b8a4" stroke-width="2.5"/></svg></div>
<div class="abs arrow-btn" style="left:1103px;top:335px"><svg width="16" height="16" viewBox="0 0 16 16"><path d="m6 2 6 6-6 6" fill="none" stroke="#33b8a4" stroke-width="2.5"/></svg></div>

<form class="abs offer-form">
  <h2>Get Your Free In Person<br>Cash Offer Today</h2>
  <div class="field">Name</div>
  <div class="field">Vehicle Type <span class="caret"></span></div>
  <div class="field-pair">
    <div class="field">Brand <span class="caret"></span></div>
    <div class="field">Year <span class="caret"></span></div>
  </div>
  <div class="field">Place
    <svg width="12" height="16" viewBox="0 0 12 16"><path d="M6 1a5 5 0 0 0-5 5c0 4 5 9 5 9s5-5 5-9a5 5 0 0 0-5-5z" fill="none" stroke="#555" stroke-width="1.5"/><circle cx="6" cy="6" r="1.8" fill="#555"/></svg>
  </div>
  <div class="field">Date and Time
    <svg width="16" height="16" viewBox="0 0 16 16"><rect x="1.5" y="3" width="13" height="11.5" fill="none" stroke="#555" stroke-width="1.4"/><path d="M1.5 6.5h13M5 1v3M11 1v3M4 9h2M7 9h2M10 9h2M4 12h2M7 12h2" stroke="#555" stroke-width="1.3"/></svg>
  </div>
  <button class="submit" type="button">Submit</button>
</form>

<!-- welcome -->
<h1 class="abs welcome-title">Welcome to FernPivotHub</h1>
<div class="abs welcome-copy">
  <p>We offer the most convenient way of selling your vehicle. We will come to you at a place of your choosing, i.e. home, office, or any other public place.&nbsp; We will give you an in person cash offer on the spot.</p>
  <ul class="checks">
    <li>Got an old clunker? I’ll But It! – Turn it into cash today!</li>
    <li>Got a nice car you just don’t need? I’ll Buy It! – Stop wasting money on insurance, registration and maintenance costs!</li>
    <li>Got a car that needs repairs? I’ll Buy It! – No matter what the issue is I’ll come take it away today!</li>
  </ul>
</div>
<div class="abs welcome-photo" role="img" aria-label="Car key being handed over to an open palm"></div>

<!-- how it works -->
<div class="abs band" style="top:1228px;height:520px;background:linear-gradient(180deg,#3f4c5c,#2b3f5c 60%,#22406a)" role="img" aria-label="Yacht on blue water beneath coastal cliffs"></div>
<svg class="abs" style="left:0;top:1228px" width="1200" height="520" viewBox="0 0 1200 520">
  <polygon points="0,0 1200,0 1200,64" fill="#fff"/>
  <polygon points="0,500 1200,430 1200,520 0,520" fill="#fff"/>
  <polygon points="110,505 1200,440 1200,465 140,520" fill="#a1cd3a"/>
</svg>
<div class="abs band-title" style="top:1334px">How it works</div>
<div class="abs step" style="left:138px;top:1390px">
  <div class="step-icon"><svg width="56" height="56" viewBox="0 0 24 24"><path fill="none" stroke="#fff" stroke-width="1.1" d="M6.6 10.8a15 15 0 0 0 6.6 6.6l2.2-2.2c.3-.3.7-.4 1-.2 1.1.4 2.3.6 3.6.6.6 0 1 .4 1 1V20c0 .6-.4 1-1 1A17 17 0 0 1 3 4c0-.6.4-1 1-1h3.5c.6 0 1 .4 1 1 0 1.3.2 2.5.6 3.6.1.3 0 .7-.2 1zM14 3a7 7 0 0 1 7 7M14 6a4 4 0 0 1 4 4"/></svg></div>
  <div class="step-num">STEP 1</div>
  <div class="step-title">Call us on 555-014-2207</div>
  <div class="step-text">Nam et tortor in ante iaculis porttitor in luctus mi.<br>Vivamus gravida sem a pretium euismod.</div>
</div>
<div class="abs step" style="left:449px;top:1390px">
  <div class="step-icon"><svg width="52" height="52" viewBox="0 0 24 24"><rect x="4" y="2" width="16" height="20" fill="none" stroke="#fff" stroke-width="1.1"/><path d="M4 5h16M8 17h8M8 19h8" stroke="#fff" stroke-width="1.1"/><circle cx="12" cy="10.5" r="2" fill="none" stroke="#fff" stroke-width="1.1"/><path d="M8.5 15a3.5 3.5 0 0 1 7 0" fill="none" stroke="#fff" stroke-width="1.1"/></svg></div>
  <div class="step-num">STEP 2</div>
  <div class="step-title">Fill out the online form</div>
  <div class="step-text">Nam et tortor in ante iaculis porttitor in luctus mi.<br>Vivamus gravida sem a pretium euismod.</div>
</div>
<div class="abs step" style="left:760px;top:1390px">
  <div class="step-icon"><svg width="58" height="58" viewBox="0 0 24 24"><path fill="none" stroke="#fff" stroke-width="1" d="M2 16V11h12v5M14 16v-6h4l3 3v3H2M3 11l5-5M5 16.5a1.5 1.5 0 1 0 3 0 1.5 1.5 0 1 0-3 0M15 16.5a1.5 1.5 0 1 0 3 0 1.5 1.5 0 1 0-3 0M15 11h2.5l2 2H15z"/></svg></div>
  <div class="step-num">STEP 3</div>
  <div class="step-title">We’ll collect your vehicle</div>
  <div class="step-text">Nam et tortor in ante iaculis porttitor in luctus mi.<br>Vivamus gravida sem a pretium euismod.</div>
</div>

<!-- reviews -->
<h2 class="abs reviews-title">Reviews</h2>
<p class="abs reviews-text">Nam fringilla nulla nisl condimentum, dapibus condimentum porta. Phasellus blandit quam a ipsum gravida dapibus. Cras sed augue tortor. Suspendisse elit ligula, iaculis dignissim justo eu, vestibulum venenatis elit. Sed egestas, nisl id cursus ultricies, turpis orci rhoncus odio, id tristique odio ex in lacus.</p>
<div class="abs avatar" role="img" aria-label="Portrait of the reviewer"></div>
<div class="abs reviewer">Mara Linden, Florida</div>
<svg class="abs" style="left:54px;top:1955px" width="20" height="28" viewBox="0 0 20 28"><path d="M16 2 4 14l12 12" fill="none" stroke="#555" stroke-width="3"/></svg>
<svg class="abs" style="left:1124px;top:1955px" width="20" height="28" viewBox="0 0 20 28"><path d="m4 2 12 12L4 26" fill="none" stroke="#555" stroke-width="3"/></svg>

<!-- why choose us -->
<div class="abs band" style="top:2144px;height:510px;background:linear-gradient(180deg,#4a5155,#353d3a 55%,#2c3330)" role="img" aria-label="Motorhome parked among pine trees at sunset"></div>
<svg class="abs" style="left:0;top:2144px" width="1200" height="512" viewBox="0 0 1200 512">
  <polygon points="0,0 1200,0 0,62" fill="#fff"/>
  <polygon points="0,425 1200,492 1200,512 0,512" fill="#fff"/>
  <polygon points="0,422 1088,480 1055,506 0,448" fill="#a1cd3a"/>
  <polygon points="0,448 1055,506 1055,512 0,512" fill="#fff"/>
</svg>
<div class="abs band-title" style="top:2274px">Why Choose Us?</div>
<div class="abs feature" style="left:143px">
  <svg width="36" height="36" viewBox="0 0 36 36"><circle cx="18" cy="18" r="17" fill="#33b8a4"/><path d="m10 18 6 6 10-11" fill="none" stroke="#fff" stroke-width="3.5"/></svg>
  <h3>Fast</h3><p>I’ll Be at Your Door Today</p>
</div>
<div class="abs feature" style="left:375px">
  <svg width="36" height="36" viewBox="0 0 36 36"><circle cx="18" cy="18" r="17" fill="#33b8a4"/><path d="m10 18 6 6 10-11" fill="none" stroke="#fff" stroke-width="3.5"/></svg>
  <h3>Fair</h3><p>Get Fair Price for Your Vehicle</p>
</div>
<div class="abs feature" style="left:606px">
  <svg width="36" height="36" viewBox="0 0 36 36"><circle cx="18" cy="18" r="17" fill="#33b8a4"/><path d="m10 18 6 6 10-11" fill="none" stroke="#fff" stroke-width="3.5"/></svg>
  <h3>Friendly</h3><p>Trusted for Over 25 Years</p>
</div>
<div class="abs feature" style="left:838px">
  <svg width="36" height="36" viewBox="0 0 36 36"><circle cx="18" cy="18" r="17" fill="#33b8a4"/><path d="m10 18 6 6 10-11" fill="none" stroke="#fff" stroke-width="3.5"/></svg>
  <h3>Hassle Free</h3><p>I Handle All the Paperwork</p>
</div>

<!-- faq -->
<h2 class="abs faq-title">FAQ</h2>
<div class="abs faq-open">
  <h4>Aenean feugiat viverra lorem ac sagittis? <span class="plus" style="background:#33b8a4;margin-top:6px">–</span></h4>
  <p>Phasellus congue dapibus sapien eu tincidunt. Duis congue mauris nec tortor elementum, scelerisque posuere felis placerat. In a ligula eu nisi sodales sollicitudin. Curabitur dignissim malesuada nibh ut euismod. In tincidunt magna nunc, id iaculis mauris condimentum et. Vestibulum id scelerisque turpis, at vulputate neque. Mauris molestie vitae orci sed condimentum.</p>
  <a>Read More</a>
</div>
<div class="abs faq-item" style="top:2965px">Etiam vel massa elementum bibendum tellus? <span class="plus">+</span></div>
<div class="abs faq-item" style="top:3037px">Cras sollicitudin cursus dui eu placerat? <span class="plus">+</span></div>
<div class="abs faq-item" style="top:3109px">Quisque aliquet ex nec est vestibulum pulvinar? <span class="plus">+</span></div>
<div class="abs faq-item" style="top:3181px">Pellentesque convallis molestie enim sit amet? <span class="plus">+</span></div>
<div class="abs faq-item" style="top:3253px">Vestibulum ante ipsum primis in faucibus orci? <span class="plus">+</span></div>
<div class="abs view-all">View All</div>

<!-- footer -->
<svg class="abs" style="left:0;top:3448px" width="1200" height="212" viewBox="0 0 1200 212">
  <polygon points="0,16 110,10 1200,58 1200,212 0,212" fill="#0f1013"/>
  <polygon points="110,0 1200,52 1200,62 0,18 0,14" fill="#a1cd3a"/>
</svg>
<div class="abs footer-links">Home<span>|</span>About Us<span>|</span>Car<span>|</span>RV<span>|</span>Boat<span>|</span>How It Works<span>|</span>Contact Us</div>
<div class="abs copyright">Copyright © 2020 &nbsp; FernPivotHub. &nbsp; All rights reserved.</div>
<div class="abs social" style="left:975px">Page</div>
<div class="abs social" style="left:1020px">Gallery</div>

</body>
</html>
```